Design for a 4 screens mobile app: Brelluvo

The app is a compact but illustrated phone/address book...
We need a design for the 5 screens of the app (see screens attached):
a) "index" : 1 screen with 6 pictures of contact person
b) "contact list" : 1 screen, to manage (add/del/edit) the contacts of the phone/address book
c) "add contact" : 1 screen to add a contact (a picture + a phone number)
d) "update contact" : similar to "add"
e) "fields missing" : add/edit screens in "error" state
We also need the ico design + loading screen.
No specific guidelines, nor logo or whatever.
It will be a free app distributed on iOS and Androïd.
We just want to make it looking nice & very usable for end users.
B2C

```html
<!DOCTYPE html>
<html lang="en">
<head>
<meta charset="utf-8">
<title>Brelluvo – Create New Contact</title>
<link href="https://fonts.googleapis.com/css2?family=Roboto:wght@400;500&display=swap" rel="stylesheet">
<style>
  :root {
    --status-bar: #1e3d68;
    --app-bar: #235084;
    --surface: #ffffff;
    --avatar-bg: #e3e3e3;
    --icon-grey: #9e9e9e;
    --text-strong: #1f1f1f;
    --text-label: #4a4a4a;
    --text-hint: #ababab;
    --divider: #e8e8e8;
    --accent: #fdd42a;
    --on-accent: #ffffff;
    --on-primary: #ffffff;
  }
  * { margin: 0; padding: 0; box-sizing: border-box; }
  html, body { width: 675px; height: 1200px; overflow: hidden; background: var(--surface); }
  body { font-family: "Roboto", Arial, sans-serif; position: relative; }

  .status-bar { position: absolute; left: 0; top: 0; width: 675px; height: 45px; background: var(--status-bar); }
  .status-bar .signal { position: absolute; left: 526px; top: 12px; }
  .status-bar .battery { position: absolute; left: 567px; top: 11px; }
  .status-bar .clock { position: absolute; left: 595px; top: 0; line-height: 45px; font-size: 22px; color: var(--on-primary); }

  .app-bar { position: absolute; left: 0; top: 45px; width: 675px; height: 105px; background: var(--app-bar);
    box-shadow: 0 3px 5px rgba(0,0,0,0.25); z-index: 2; }
  .app-bar .back { position: absolute; left: 33px; top: 34px; }
  .app-bar .title { position: absolute; left: 105px; top: 0; line-height: 105px; font-size: 33px; color: var(--on-primary); font-weight: 400; }

  .photo-picker { position: absolute; left: 0; top: 150px; width: 675px; height: 400px; }
  .photo-picker .gallery { position: absolute; left: 98px; top: 149px; }
  .photo-picker .avatar { position: absolute; left: 228px; top: 57px; width: 219px; height: 219px; border-radius: 50%;
    background: var(--avatar-bg); display: flex; align-items: center; justify-content: center; }
  .photo-picker .settings { position: absolute; left: 537px; top: 142px; }

  .contact-name { position: absolute; left: 0; top: 466px; width: 675px; text-align: center; font-size: 33px; line-height: 44px; color: var(--text-strong); }

  .phone-field { position: absolute; left: 100px; right: 0; }
  .phone-field .label { font-size: 26px; line-height: 34px; color: var(--text-label); }
  .phone-field .value { margin-top: 20px; font-size: 27px; line-height: 34px; color: var(--text-hint); }
  .field-work { top: 588px; height: 114px; border-bottom: 1px solid var(--divider); }
  .field-home { top: 724px; }

  .save-button { position: absolute; left: 36px; top: 1012px; width: 612px; height: 113px; border: 0; border-radius: 4px;
    background: var(--accent); color: var(--on-accent); font-family: "Roboto", Arial, sans-serif; font-size: 38px; font-weight: 500;
    letter-spacing: 0.5px; }
</style>
</head>
<body>
  <header class="status-bar">
    <svg class="signal" width="22" height="22" viewBox="0 0 22 22" aria-hidden="true"><path d="M22 0V22H0Z" fill="#ffffff"/></svg>
    <svg class="battery" width="14" height="23" viewBox="0 0 14 23" aria-hidden="true"><rect x="4" y="0" width="6" height="3" fill="#ffffff"/><rect x="0" y="2" width="14" height="21" rx="1" fill="#ffffff"/></svg>
    <span class="clock">12:30</span>
  </header>

  <nav class="app-bar">
    <svg class="back" width="36" height="36" viewBox="0 0 24 24" aria-label="Back"><path d="M20 11H7.8l5.6-5.6L12 4l-8 8 8 8 1.4-1.4L7.8 13H20z" fill="#ffffff"/></svg>
    <h1 class="title">Create New Contact</h1>
  </nav>

  <section class="photo-picker">
    <svg class="gallery" width="38" height="34" viewBox="0 0 38 34" aria-label="Choose from gallery">
      <rect x="0" y="0" width="38" height="34" rx="2" fill="var(--icon-grey)"/>
      <rect x="3" y="3" width="32" height="28" fill="#ffffff"/>
      <path d="M4 30 L13 19 L19 26 L25 18 L34 30 Z" fill="var(--icon-grey)"/>
    </svg>
    <div class="avatar">
      <svg width="80" height="70" viewBox="0 0 80 70" aria-label="Take a photo">
        <path d="M26 0h28l6 10h14a6 6 0 0 1 6 6v48a6 6 0 0 1-6 6H6a6 6 0 0 1-6-6V16a6 6 0 0 1 6-6h14z" fill="#ffffff"/>
        <circle cx="40" cy="39" r="16" fill="var(--avatar-bg)"/>
      </svg>
    </div>
    <svg class="settings" width="38" height="38" viewBox="0 0 24 24" aria-label="Settings">
      <path fill="var(--icon-grey)" d="M19.4 13a7.5 7.5 0 0 0 0-2l2.1-1.6-2-3.5-2.5 1a7 7 0 0 0-1.7-1l-.4-2.6h-4l-.4 2.6a7 7 0 0 0-1.7 1l-2.5-1-2 3.5L4.6 11a7.5 7.5 0 0 0 0 2l-2.1 1.6 2 3.5 2.5-1a7 7 0 0 0 1.7 1l.4 2.6h4l.4-2.6a7 7 0 0 0 1.7-1l2.5 1 2-3.5zM12 15.5a3.5 3.5 0 1 1 0-7 3.5 3.5 0 0 1 0 7z"/>
    </svg>
  </section>

  <h2 class="contact-name">Add A Name</h2>

  <div class="phone-field field-work">
    <p class="label">Work</p>
    <p class="value">000-000-0000</p>
  </div>
  <div class="phone-field field-home">
    <p class="label">Home</p>
    <p class="value">000-000-0000</p>
  </div>

  <button class="save-button">SAVE</button>
</body>
</html>
```